Kettle Pine Society - A Monthly Subscription Coffee Club - Shopify Website Design

A monthly subscription company. Need a Shopify Website Design and uploaded to fully work with Tidewell Renewals.

Please look at these sites for examples as well as the images I enclosed.

https://www.sipvaultory.com/
https://crumbcrate.com/
https://www.platewindly.com/
https://www.globalnibblers.com/

Number of Pages Required

1 page

```html
<!DOCTYPE html>
<html lang="en">
<head>
<meta charset="utf-8">
<title>Kettle Pine Society – Monthly Coffee Club</title>
<link href="https://fonts.googleapis.com/css2?family=Poppins:wght@500;600;700;800&family=Open+Sans:wght@400;600;700&display=swap" rel="stylesheet">
<style>
:root{
  --espresso:#3b1a12;
  --roast:#7b3a2c;
  --roast-dark:#5a2a1f;
  --mocha:#8a5a3c;
  --crema:#c9a27a;
  --price:#a46b52;
  --ink:#1c1c1c;
  --muted:#777;
  --paper:#ffffff;
  --line:#e5e5e5;
}
*{box-sizing:border-box;margin:0;padding:0}
html,body{width:1200px;height:3492px;overflow:hidden;background:var(--paper)}
body{font-family:"Open Sans",sans-serif;color:var(--ink)}
h1,h2,h3,h4,.brand,.nav a,.btn{font-family:"Poppins",sans-serif}

/* header */
.site-header{height:60px;display:flex;align-items:center;justify-content:space-between;padding:0 64px 0 110px}
.brand{display:flex;align-items:center;gap:10px;font-weight:700;font-size:17px;color:var(--espresso);text-transform:uppercase}
.brand-dot{width:20px;height:20px;border-radius:50%;background:var(--roast)}
.nav{display:flex;align-items:center;gap:22px}
.nav a{font-size:14px;color:var(--ink);text-decoration:none;font-weight:500}
.nav a.active{border-bottom:2px solid var(--ink);padding-bottom:2px}
.nav-icons{display:flex;gap:14px;margin-left:16px}

/* hero */
.hero{position:relative;height:540px;background:linear-gradient(100deg,#8a6a4c 0%,#a68662 40%,#7a3226 62%,#b0192a 78%,#5a3a26 100%)}
.hero .photo{position:absolute;inset:0}
.hero-copy{position:absolute;left:110px;top:180px;color:#fff;width:440px}
.hero-copy h1{font-size:40px;font-weight:700;text-transform:uppercase;letter-spacing:.5px}
.hero-copy p{font-size:15px;font-weight:600;line-height:1.4;margin:10px 0 26px}
.btn{display:inline-block;background:var(--roast);color:#fff;font-size:13px;font-weight:600;text-transform:uppercase;padding:11px 22px;border-radius:2px}
.btn.dark{background:var(--espresso)}
.hero-dots{position:absolute;left:590px;bottom:70px;display:flex;gap:6px}
.hero-dots span{width:8px;height:8px;border-radius:50%;background:#fff;opacity:.5}
.hero-dots span:first-child{opacity:1}

/* sections */
.section-title{text-align:center;font-size:32px;font-weight:700;text-transform:uppercase}
.rule{width:40px;height:2px;background:var(--ink);margin:10px auto 0}
.intro{text-align:center;font-size:13px;color:var(--muted);line-height:1.6;width:880px;margin:22px auto 0}

.how{height:608px;padding-top:72px}
.steps{display:flex;justify-content:center;gap:12px;margin-top:28px}
.step{width:316px;text-align:center}
.step .photo{height:208px}
.step h3{font-size:18px;font-weight:600;margin-top:26px;font-family:"Open Sans",sans-serif}
.step:not(:first-child) h3{text-transform:uppercase;font-weight:700}

.box{position:relative;height:440px;background:linear-gradient(90deg,#a0754c 0%,#8a5a3a 35%,#6a4128 60%,#5a3621 100%)}
.box .photo{position:absolute;inset:0}
.box-copy{position:absolute;left:600px;top:72px;width:470px;color:#fff}
.box-copy h2{font-size:36px;font-weight:700;text-transform:uppercase}
.box-copy p{font-size:13px;line-height:1.65;margin:14px 0 24px}

.products{height:532px;padding-top:88px}
.product-grid{display:flex;justify-content:center;gap:64px;margin-top:52px}
.product{width:180px;text-align:center}
.product .photo{height:140px;margin:0 20px}
.product h4{font-size:15px;font-weight:700;text-transform:uppercase;margin-top:24px}
.product .price{font-size:17px;color:var(--price);margin-top:4px}

.plans{position:relative;height:320px;background:linear-gradient(90deg,#2e1a10 0%,#5a3620 40%,#7a4a2a 70%,#3a2414 100%);color:#fff;text-align:center}
.plans .photo{position:absolute;inset:0}
.plans-copy{position:absolute;left:0;right:0;top:72px}
.plans-copy h2{font-size:32px;font-weight:700;text-transform:uppercase}
.plans-copy p{font-size:13px;line-height:1.6;width:720px;margin:10px auto 24px}

.news{height:640px;padding-top:68px}
.news-grid{display:flex;justify-content:center;gap:12px;margin-top:48px}
.post{width:316px}
.post .photo{height:212px}
.post h3{font-size:16px;font-weight:700;text-transform:uppercase;margin:38px 20px 0;font-family:"Open Sans",sans-serif}
.post .date{font-size:10px;color:var(--price);text-transform:uppercase;margin:10px 20px 0;letter-spacing:.5px}
.post p{font-size:11px;color:var(--muted);line-height:1.6;margin:10px 20px 0}

/* footer */
.site-footer{height:352px;background:var(--espresso);color:#fff;display:flex;padding:62px 0 0 110px}
.follow{width:420px}
.site-footer h4{font-size:15px;font-weight:700;text-transform:uppercase}
.socials{display:flex;gap:10px;margin:20px 0 16px}
.socials span{width:34px;height:34px;border-radius:50%;background:#8a6a5e}
.follow p{font-size:11px;line-height:1.6;color:#e4d8d2;width:320px}
.footer-main{width:550px}
.footer-links{display:flex;gap:18px}
.footer-main .lead{font-size:11px;color:#e4d8d2;margin:16px 0 14px}
.signup{display:grid;grid-template-columns:262px 262px;gap:10px 10px}
.signup span{height:30px;background:#fff;color:#888;font-size:11px;padding:8px 10px}
.signup .submit{background:var(--roast);color:#fff;text-align:center;font-weight:700;text-transform:uppercase;font-family:"Poppins",sans-serif}
.copyright{font-size:11px;color:#e4d8d2;margin:24px 0 14px}
.cards{display:flex;gap:6px}
.cards span{width:34px;height:22px;border-radius:3px;background:#f2ece8}
</style>
</head>
<body>

<header class="site-header">
  <div class="brand"><span class="brand-dot"></span>Kettle Pine Society</div>
  <nav class="nav">
    <a class="active">Home</a><a>Our Plans</a><a>How It Works</a><a>Our Menus</a><a>Gift Cards</a>
    <span class="nav-icons">
      <svg width="16" height="16" viewBox="0 0 16 16"><circle cx="8" cy="8" r="7" fill="none" stroke="#1c1c1c" stroke-width="1.5"/><circle cx="8" cy="6" r="2.5" fill="#1c1c1c"/><path d="M3.5 13c1-2.5 8-2.5 9 0" fill="#1c1c1c"/></svg>
      <svg width="16" height="16" viewBox="0 0 16 16"><circle cx="7" cy="7" r="5" fill="none" stroke="#1c1c1c" stroke-width="2"/><path d="M11 11l4 4" stroke="#1c1c1c" stroke-width="2"/></svg>
      <svg width="18" height="16" viewBox="0 0 18 16"><path d="M1 1h3l2 9h9l2-7H5" fill="none" stroke="#1c1c1c" stroke-width="1.8"/><circle cx="7" cy="14" r="1.5" fill="#1c1c1c"/><circle cx="14" cy="14" r="1.5" fill="#1c1c1c"/></svg>
    </span>
  </nav>
</header>

<section class="hero">
  <div class="photo" role="img" aria-label="Red gift box filled with roasted coffee beans and a heart-shaped biscuit beside a cup of coffee on burlap"></div>
  <div class="hero-copy">
    <h1>Kettle Pine Society</h1>
    <p>Lorem ipsum dolor sit amet, consectetur adipiscing elit, sed do eiusmod tempor incididunt</p>
    <span class="btn">Shop Now</span>
  </div>
  <div class="hero-dots"><span></span><span></span></div>
</section>

<section class="how">
  <h2 class="section-title">How It Works</h2>
  <div class="rule"></div>
  <p class="intro">Sed ut perspiciatis unde omnis iste natus error sit voluptatem accusantium doloremque laudantium, totam rem aperiam, eaque ipsa quae ab illo inventore veritatis et quasi architecto beatae vitae.</p>
  <div class="steps">
    <div class="step"><div class="photo" role="img" aria-label="Hands holding fresh coffee beans" style="background:linear-gradient(135deg,#c9b9a6,#6b4a36)"></div><h3>Lorem ipsum dolor sit</h3></div>
    <div class="step"><div class="photo" role="img" aria-label="Wooden crate of coffee beans with a cup" style="background:linear-gradient(135deg,#e8e0d6,#8a6244)"></div><h3>Lorem ipsum dolor sit</h3></div>
    <div class="step"><div class="photo" role="img" aria-label="Close view of roasted coffee beans" style="background:linear-gradient(135deg,#9a6a44,#4a2a18)"></div><h3>Lorem ipsum dolor sit</h3></div>
  </div>
</section>

<section class="box">
  <div class="photo" role="img" aria-label="Kraft gift boxes tied with brown ribbon next to paper coffee cups and beans"></div>
  <div class="box-copy">
    <h2>What's Inside the Box</h2>
    <p>Lorem ipsum dolor sit amet, consectetur adipiscing elit, sed do eiusmod tempor incididunt ut labore et dolore magna aliqua. Ut enim ad minim veniam, quis nostrud exercitation ullamco. Sed ut perspiciatis unde omnis iste natus error sit voluptatem accusantium doloremque laudantium, totam rem aperiam.</p>
    <span class="btn dark">Choose Your Plan</span>
  </div>
</section>

<section class="products">
  <h2 class="section-title">Featured Products</h2>
  <div class="product-grid">
    <div class="product"><div class="photo" role="img" aria-label="Black coffee gift box" style="background:linear-gradient(180deg,#fff 20%,#2a2a2a 45%,#111 80%,#fff 80%)"></div><h4>Product Title</h4><div class="price">$67.00</div></div>
    <div class="product"><div class="photo" role="img" aria-label="Coffee sampler box" style="background:linear-gradient(180deg,#fff 25%,#2a1a12 40%,#c9a27a 75%,#fff 75%)"></div><h4>Product Title</h4><div class="price">$67.00</div></div>
    <div class="product"><div class="photo" role="img" aria-label="Bag of ground coffee" style="background:linear-gradient(90deg,#fff 30%,#1a1a1a 30%,#3a2a1a 70%,#fff 70%)"></div><h4>Product Title</h4><div class="price">$67.00</div></div>
    <div class="product"><div class="photo" role="img" aria-label="Wooden coffee gift chest" style="background:linear-gradient(180deg,#fff 15%,#7a4a26 30%,#4a2a16 85%,#fff 85%)"></div><h4>Product Title</h4><div class="price">$67.00</div></div>
  </div>
</section>

<section class="plans">
  <div class="photo" role="img" aria-label="Coffee beans scattered across a dark background"></div>
  <div class="plans-copy">
    <h2>Flexible Plans</h2>
    <p>Lorem ipsum dolor sit amet, consectetur adipiscing elit, sed do eiusmod tempor incididunt ut labore et dolore magna aliqua. Ut enim ad minim veniam, quis nostrud exercitation ullamco laboris.</p>
    <span class="btn dark">View Our Plan</span>
  </div>
</section>

<section class="news">
  <h2 class="section-title">Latest News</h2>
  <div class="rule"></div>
  <div class="news-grid">
    <article class="post"><div class="photo" role="img" aria-label="Vintage coffee grinder with beans" style="background:linear-gradient(135deg,#a07050,#3a1e12)"></div><h3>Lorem ipsum dolor</h3><div class="date">October 15, 2020</div><p>At vero eos et accusamus et iusto odio dignissimos ducimus qui blanditiis praesentium voluptatum deleniti atque.</p></article>
    <article class="post"><div class="photo" role="img" aria-label="Cup of coffee on a saucer with beans" style="background:linear-gradient(135deg,#8a5a38,#e8e0d8 60%,#5a3422)"></div><h3>Lorem ipsum dolor</h3><div class="date">October 15, 2020</div><p>At vero eos et accusamus et iusto odio dignissimos ducimus qui blanditiis praesentium voluptatum deleniti atque.</p></article>
    <article class="post"><div class="photo" role="img" aria-label="Wooden tray with compartments of different coffee beans" style="background:linear-gradient(135deg,#c9ad88,#6a4a30)"></div><h3>Lorem ipsum dolor</h3><div class="date">October 15, 2020</div><p>At vero eos et accusamus et iusto odio dignissimos ducimus qui blanditiis praesentium voluptatum deleniti atque.</p></article>
  </div>
</section>

<footer class="site-footer">
  <div class="follow">
    <h4>Follow</h4>
    <div class="socials"><span></span><span></span><span></span></div>
    <p>At vero eos et accusamus et iusto odio dignissimos ducimus qui blanditiis praesentium voluptatum</p>
  </div>
  <div class="footer-main">
    <div class="footer-links"><h4>About Us</h4><h4>Our Products</h4><h4>Contact Us</h4></div>
    <p class="lead">Sign up to our newsletter below to keep in touch with us</p>
    <div class="signup">
      <span>First Name</span><span>Last Name</span>
      <span>Email Address</span><span class="submit">Sign Up</span>
    </div>
    <p class="copyright">© 2020, Kettle Pine Society. All Rights Reserved</p>
    <div class="cards"><span></span><span></span><span></span><span></span><span></span><span></span><span></span></div>
  </div>
</footer>

</body>
</html>
```